"Crestline Shape Trim Method" eBook cover

THE TITLE HAS CHANGED SLIGHTLY TO ;
"Crestline Shape Trim Method"

The following is for a fat loss, health and fitness eBook titled "Crestline Shape Trim Method." This design should help promote and market this product, as well as intrigue those to not only make a purchase... but want to very much participate in the material and follow the material!

There is no restriction of color, idea, etc. PLEASE help me with your expertise in developing a great cover for this project...

THANKS SO MUCH

This book separates others just by the quality information provided. To much trial and error is wasted on false claims and overrated programs....I have provided the books topics below to hopefully give you a better understanding;
CHAPTER 1
Crestline Shape Trim Guide
- What is it?
- Why it works?
- Why it will work for you?
CHAPTER 2
Kill Cardio
- Why cardio sucks?
- Myth about cardio?
- What cardio works for fat loss
CHAPTER 3
Iron vs. Machine
- What type of resistance training is best for fat loss?
- Why?
- The big pitfall to working on machines?
CHAPTER 4
Should You Really Eat That?
- Foods that build muscle
- Foods that burn fat
- Foods that suck!
CHAPTER 5
Playing With Iron
- Playing with iron
- 17 upper body builders
- 17 lower body builders
- 11 workouts in 11 minutes
CHAPTER 6
Buying Equipment On A Budget
- How to find dirt cheap dumbbells?
- How to build equipment under $100

THANKS AGAIN!

Target Market(s)

Self-Help / Health And Fitness / Nutrition

Industry/Entity Type

Health And Wellness

Font styles to use
Serif
Sans Serif
Other font styles liked:
• Tahoma, Verdana, Calibri

Requirements
Must have
• MUST MEET VORELLO.com GUIDLINES ;
• File Types
• Pagewell Direct Publishing currently accepts two types of files for cover images:
• JPEG (JPEG / JPG)
• TIFF (TIF / TIFF)
• We apply additional compression to images when displaying them on the website. For best results, please upload your images with minimal compression.
• Dimensions
• Requirements for the size of your cover art must have an ideal height/width ratio of at least 8:5 (1.6), meaning:
• • A minimum of 625 pixels on the shortest side and 1000 pixels on the longest side
• • For best quality, your image should be 2500 pixels on the longest side
• Important: We cannot accept any images larger than 10,000 pixels on the longest side.
• Size
• Your cover image must be less than 50MB. If the file type you are using supports compression, make sure to enable as little compression as possible, e.g. none for TIFF. Be sure to save your file with 72 dots per inch (DPI).
• Color
• Product images display on the Vorello website using the RGB (red, green, blue) color mode or profile. RGB is the color mode native to the web and many color screen displays, as these three colors displayed at varying levels of intensity create over 16 million colors. When saving and uploading your cover image file, save your file ONLY as RGB - not CMYK or sRGB- for the color profile. You can usually find this option in the File saving dialog of image manipulation programs such as Photoshop.
• Some programs may also refer to RGB color as 'True Color' in some programs. If in doubt, try opening a JPG inside Internet Explorer, Firefox, or Safari. If a JPG opens fine inside a web browser, it's most likely okay to use as a cover image.
• Make sure to save your image without color separation. This is usually a pre-press or color palette option. Use your image manipulation program or image analysis tool (some are available free online) to verify that your image file doesn't have color separation.
• Use color images whenever possible and relevant. In addition to the Pagewell black and white E Ink reading devices, customers can read your books on full color Lumo devices and free Pagewell reading apps for iPhone, iPad, Android, PC or Mac.
Should not have
• NO MALE OR FEMALE MODLES OR HALF NAKED PEOPLE...

```html
<!DOCTYPE html>
<html lang="en">
<head>
<meta charset="utf-8">
<title>Crestline Shape Trim Method — eBook Cover</title>
<link rel="stylesheet" href="https://fonts.googleapis.com/css2?family=Open+Sans:wght@400;500&display=swap">
<style>
  :root {
    --sky-top: #b9c8c2;
    --sky-haze: #f5e7de;
    --sky-glow: #f8ece4;
    --ridge-blue: #86a19f;
    --hill-green: #7a8a63;
    --meadow-gold: #b9a15e;
    --grass-brown: #8a6a3a;
    --title-peach: #d98a6a;
    --title-black: #111111;
    --title-white: #ffffff;
  }
  * { margin: 0; padding: 0; box-sizing: border-box; }
  html, body {
    width: 750px;
    height: 1200px;
    overflow: hidden;
    background: #ffffff;
  }
  .cover {
    position: relative;
    width: 750px;
    height: 1200px;
    overflow: hidden;
    font-family: "Open Sans", Calibri, sans-serif;
  }
  .cover__landscape {
    position: absolute;
    inset: 0;
    background:
      linear-gradient(180deg,
        var(--sky-top) 0%,
        #d8d9cf 12%,
        var(--sky-haze) 26%,
        var(--sky-glow) 36%,
        #e4ddd4 40%,
        var(--ridge-blue) 44%,
        #95a99c 50%,
        var(--hill-green) 56%,
        #8f9466 62%,
        var(--meadow-gold) 70%,
        #a98c52 82%,
        var(--grass-brown) 100%);
  }
  .title {
    position: absolute;
    top: 0;
    left: 0;
    width: 100%;
    text-align: center;
    line-height: 1;
  }
  .title__line { display: block; }
  .title__crestline {
    position: absolute;
    top: 42px;
    width: 100%;
    font-size: 82px;
    font-weight: 400;
    color: var(--title-peach);
    letter-spacing: 1px;
  }
  .title__shape {
    position: absolute;
    top: 118px;
    width: 100%;
    font-size: 156px;
    font-weight: 400;
    color: var(--title-peach);
  }
  .title__trim {
    position: absolute;
    top: 262px;
    width: 100%;
    font-size: 210px;
    font-weight: 400;
    color: var(--title-black);
  }
  .title__method {
    position: absolute;
    top: 548px;
    width: 100%;
    font-size: 96px;
    font-weight: 400;
    color: var(--title-white);
    letter-spacing: 18px;
    padding-left: 18px;
  }
  .author {
    position: absolute;
    top: 1122px;
    width: 100%;
    text-align: center;
    font-size: 30px;
    font-weight: 400;
    color: var(--title-white);
    letter-spacing: 5px;
    padding-left: 5px;
  }
</style>
</head>
<body>
  <main class="cover">
    <div class="cover__landscape" role="img" aria-label="Photograph of a hazy sky over blue mountain ridges and a green hill, with a golden grass meadow in the foreground"></div>
    <h1 class="title">
      <span class="title__line title__crestline">CRESTLINE</span>
      <span class="title__line title__shape">SHAPE</span>
      <span class="title__line title__trim">TRIM</span>
      <span class="title__line title__method">METHOD</span>
    </h1>
    <p class="author">AUTHOR’S NAME</p>
  </main>
</body>
</html>
```